Harrowby Wine Label - Design a front and smaller back label for an exclusive red wine

Harrowby Wines produces a very high quality, high priced wine from an old and prestigous vineyard in one of Australia's oldest, but smallest wine growing regions. The grapevines are old (like old men with gnarled arms and trunks) and they produce fewer grapes than younger vines but the grape quality (and thus wine quality) is magnificent and highly sought after as it produces wine of exceptional quality.
The vineyard was purchased by the Harrowby family in February 2010 from a multinational wine company who made wonderful, trophy winning wines for 10 years before the vineyard went into a decline.
The challenge is to produce 2 labels - a simple main front label that focuses on the Harrowby brand and a smaller, information rich, back label that relates the history of the vineyard.
The labels should have a white or charcoal grey background and impart tradition, quality, exclusivity and a little self indulgence which is why we want the family crest incorporated - the choice of font will help.
It might also impart a sense of fun so that it appeals to the 25-35 year old age bracket.
The label should be kept clean and simple not loud and busy. Preferred colours are black, grey and white. Red is fine if used sparingly

Here are the details:_

Front Label (115 long x 65-90mm wide)

Harrowby
Lanternwatch Reserve
2011
Mudgee
Wine of Australia 750ml

Back Label (dimensions to suit text and front label design; font size small; text in black so that it is readable in less than optimal light (eg candlelight at a restaurant table).

Harrowby
Lanternwatch Reserve 2011

This is the first release of The Lanternwatch’s Reserve – just 100 dozen bottles were made. The wine was made from Shiraz and 10% Cabernet Sauvignon grapes sourced from an iconic Mudgee vineyard that was established 1966 by Peter Vallis. In 1994, the vineyard known as ”Silver Hollow”, became the source of a decade of formidable, trophy winning wines under Tindalberg’s and later Quellwood’s ownership. The 20ha vineyard was purchased by Corin & Margaret Harrowby in 2010. The Silver Hollow name was retained by Quellwoods; no wine has been released under this label since the 2006 vintage.

The shaky old Shiraz vines are slowly being restored to full health using careful cane pruning techniques that stimulates fresh, new tissue growth, more even bunch sizes and better grape quality and consistency. The Shiraz grapes used in this wine were hand-picked from two rows of the first crop from the 46 year old, cane pruned vines. The 2011 Reserve is the first step to re-establish the traditions of a famous vineyard and one of Australia’s most sought after export wines.

“Deep and intense purple hues with aromas of ripe blackberry fruits, spice and eucalypt with rich chocolate complemented by subtle oak overtones. A rich and full bodied wine exhibiting a soft yet generous palate with plum, forest fruits and mint chocolate notes. A fine grained tannin structure displaying integrated oak characters adds to the complexity of the wine. This wine was aged for 18 months in a blend of new French oak hogsheads and one year old American hogsheads, crafting a blend with great structure and length of flavour which will develop into a Mudgee classic” – Lewis Farrant, Winemaker

13.5% Alc/Vol.
Contains approx 8.0 std drinks
Preservative (220) added

Harrowby Wines
Tallowbend Rd, Mudgee 2850
www.harrowbywines.example.au

Reason: My apologies to the designers who have kindly submitted some wonderful designs. I am trying to achieve a conscentious between shareholders. This is difficult as they are in different parts of the world and I have learned through this experience that opinions on wine labels are quite diverse!!! The feedback I have received so far indicates the following (1) A light or white background is preferred (2) The crest should not be a dominant part of the label (3) The label needs to be clean, fresh and uncomplicated (4) If red is used it should be in minor detail only (5) "Harrowby" should be distinctive. The font is difficult for us! (6) We are considering "The Lanternwatch" RESERVE instead of "Lanternwatch's" RESERVE (7) The text on the back label is too long; I will edit and re-upload Many thanks for your help and patience Kind regards Corin

Good Morning All,
I have edited the back label text to reduce the size of the label. A Word file with the changes has just been uploaded.
Cheers
Corin

Dear Designers,
Thank you all so very much for the wonderful selection of designs you have submitted my family have all been overwhelmed by the quality and skill level exhibited and we all appreciate you your efforts
Kindest regards
Corin

Target Market(s)

25-35 year old men and women of Australia, China, US & UK

Industry/Entity Type

Restaurant

Requirements
Must have
• Crest
Should not have
• Animals on the label

```html
<!DOCTYPE html>
<html lang="en">
<head>
<meta charset="utf-8">
<title>Harrowby Wine Label – The Lanternwatch's Reserve 2011</title>
<link rel="stylesheet" href="https://fonts.googleapis.com/css2?family=Pinyon+Script&family=Cormorant+Garamond:wght@400;500&family=Tinos&family=Arimo&display=swap">
<style>
  :root {
    --brick: #8c8c8c;
    --paper: #ffffff;
    --wine-red: #8b1212;
    --ink: #1c1c1c;
    --ink-soft: #444444;
    --crest-tone: #d9d9d9;
  }
  html, body {
    margin: 0;
    padding: 0;
    width: 1200px;
    height: 1091px;
    overflow: hidden;
    background: var(--paper);
  }
  .canvas {
    position: relative;
    width: 703px;
    height: 639px;
    transform: scale(1.70697);
    transform-origin: 0 0;
    color: var(--ink);
  }
  .masonry {
    position: absolute;
    inset: 0;
    width: 703px;
    height: 639px;
  }
  .masonry .brick { fill: var(--brick); }
  .masonry .joint { stroke: var(--paper); stroke-width: 3; }
  .masonry .keystone-red { fill: var(--wine-red); }

  .label-text {
    position: absolute;
    text-align: center;
    margin: 0;
    white-space: nowrap;
  }
  .script { font-family: "Pinyon Script", cursive; font-weight: 400; color: var(--ink-soft); }
  .serif { font-family: "Cormorant Garamond", serif; }

  /* Front label */
  .front-brand   { left: 42px; width: 266px; top: 118px; font-size: 50px; line-height: 1; }
  .front-title   { left: 42px; width: 266px; top: 226px; font-size: 37px; line-height: 45px; color: var(--wine-red); font-weight: 500; }
  .front-vintage { left: 42px; width: 266px; top: 366px; font-size: 24px; line-height: 1; font-family: "Tinos", serif; }
  .front-region  { left: 42px; width: 266px; top: 402px; font-size: 34px; line-height: 1; }
  .front-crest   { position: absolute; left: 142px; top: 462px; width: 66px; height: 110px; }
  .front-origin  { left: 42px; width: 266px; top: 586px; font-size: 15px; line-height: 20px; font-family: "Tinos", serif; color: var(--ink-soft); }

  /* Back label */
  .back-brand   { left: 394px; width: 267px; top: 84px; font-size: 30px; line-height: 1; }
  .back-title   { left: 394px; width: 267px; top: 130px; font-size: 17px; line-height: 1; color: var(--wine-red); font-variant: small-caps; font-weight: 500; letter-spacing: .2px; }
  .back-vintage { left: 394px; width: 267px; top: 150px; font-size: 13px; line-height: 1; font-family: "Tinos", serif; color: var(--ink-soft); }
  .back-story {
    position: absolute;
    left: 437px;
    width: 216px;
    top: 180px;
    font-family: "Tinos", serif;
    font-size: 9.9px;
    line-height: 11.6px;
    text-align: left;
  }
  .back-story p { margin: 0 0 11.6px; }
  .back-maker   { left: 394px; width: 267px; top: 505px; font-size: 19px; line-height: 1; }
  .back-address { left: 394px; width: 267px; top: 528px; font-family: "Tinos", serif; font-size: 11px; line-height: 13px; }
  .back-address .road { font-variant: small-caps; font-size: 12.5px; letter-spacing: .4px; }
  .back-facts   { left: 394px; width: 267px; top: 565px; font-family: "Arimo", sans-serif; font-size: 8.6px; line-height: 10.4px; }
</style>
</head>
<body>
<main class="canvas">
  <svg class="masonry" viewBox="0 0 703 639" aria-hidden="true">
    <defs>
      <g id="brick-column">
        <rect class="brick" x="0" y="188" width="42" height="23"/>
        <rect class="brick" x="0" y="214" width="42" height="23"/>
        <rect class="brick" x="0" y="240" width="42" height="23"/>
        <rect class="brick" x="0" y="266" width="42" height="23"/>
        <rect class="brick" x="0" y="318" width="42" height="23"/>
        <rect class="brick" x="0" y="344" width="42" height="23"/>
        <rect class="brick" x="0" y="370" width="42" height="23"/>
        <rect class="brick" x="0" y="396" width="42" height="23"/>
        <rect class="brick" x="0" y="422" width="42" height="23"/>
        <rect class="brick" x="0" y="448" width="42" height="23"/>
        <rect class="brick" x="0" y="474" width="42" height="23"/>
        <rect class="brick" x="0" y="500" width="42" height="23"/>
        <rect class="brick" x="0" y="526" width="42" height="23"/>
        <rect class="brick" x="0" y="552" width="42" height="23"/>
        <rect class="brick" x="0" y="578" width="42" height="23"/>
        <rect class="brick" x="0" y="604" width="42" height="23"/>
        <rect class="brick" x="0" y="630" width="42" height="9"/>
        <rect class="keystone-red" x="7" y="292" width="28" height="23"/>
      </g>
      <g id="brick-arch">
        <path class="brick" d="M0 186 A175 175 0 0 1 350 186 L308 186 A133 133 0 0 0 42 186 Z"/>
        <g class="joint">
          <line x1="44" y1="185" x2="-4" y2="185" transform="rotate(13.85 175 185)"/>
          <line x1="44" y1="185" x2="-4" y2="185" transform="rotate(27.7 175 185)"/>
          <line x1="44" y1="185" x2="-4" y2="185" transform="rotate(41.55 175 185)"/>
          <line x1="44" y1="185" x2="-4" y2="185" transform="rotate(55.4 175 185)"/>
          <line x1="44" y1="185" x2="-4" y2="185" transform="rotate(69.25 175 185)"/>
          <line x1="44" y1="185" x2="-4" y2="185" transform="rotate(83.1 175 185)"/>
          <line x1="44" y1="185" x2="-4" y2="185" transform="rotate(96.9 175 185)"/>
          <line x1="44" y1="185" x2="-4" y2="185" transform="rotate(110.75 175 185)"/>
          <line x1="44" y1="185" x2="-4" y2="185" transform="rotate(124.6 175 185)"/>
          <line x1="44" y1="185" x2="-4" y2="185" transform="rotate(138.45 175 185)"/>
          <line x1="44" y1="185" x2="-4" y2="185" transform="rotate(152.3 175 185)"/>
          <line x1="44" y1="185" x2="-4" y2="185" transform="rotate(166.15 175 185)"/>
        </g>
      </g>
    </defs>
    <use href="#brick-arch"/>
    <use href="#brick-column"/>
    <use href="#brick-column" x="308"/>
    <use href="#brick-arch" x="353"/>
    <use href="#brick-column" x="353"/>
    <use href="#brick-column" x="661"/>
  </svg>

  <section class="front-label">
    <h1 class="label-text script front-brand">Harrowby</h1>
    <h2 class="label-text serif front-title">The<br>Lanternwatch’s<br>Reserve</h2>
    <p class="label-text front-vintage">2011</p>
    <p class="label-text script front-region">Mudgee</p>
    <svg class="front-crest" viewBox="0 0 66 110" role="img" aria-label="Harrowby family crest">
      <rect width="66" height="110" fill="var(--crest-tone)"/>
    </svg>
    <p class="label-text front-origin">Wine of Australia<br>750ml</p>
  </section>

  <section class="back-label">
    <h1 class="label-text script back-brand">Harrowby</h1>
    <h2 class="label-text serif back-title">The Lanternwatch Reserve</h2>
    <p class="label-text back-vintage">2011</p>
    <div class="back-story">
      <p>The Shiraz and Cabernet grapes from which this wine was made were handpicked from a 20ha vineyard that was established in 1966. The vineyard formerly known as “Silver Hollow” was purchased by the Harrowby family in 2010.</p>
      <p>The shaky old Shiraz vines are slowly being restored to full health using careful cane pruning techniques to achieve better grape quality and consistency. The 2011 Reserve is the first step to re-establish the traditions of a famous vineyard and one of Australia’s most sought after export wines.</p>
      <p>“Deep and intense purple hues with aromas of ripe blackberry fruits, spice and eucalypt with rich chocolate complemented by subtle oak overtones. A rich and full bodied wine exhibiting a soft yet generous palate with plum, forest fruits and mint chocolate notes. A fine grained tannin structure displaying integrated oak characters adds to the complexity of the wine. This wine was aged for 18 months in a blend of new French oak hogsheads and one year old American hogsheads, crafting a blend with great structure and length of flavour which will develop into a Mudgee classic” - Lewis Farrant, Winemaker.</p>
    </div>
    <p class="label-text script back-maker">Harrowby Wines</p>
    <p class="label-text back-address"><span class="road">Tallowbend Rd. Mudgee 2850</span><br>www.harrowbywines.example.au</p>
    <p class="label-text back-facts">13.5% Alc/Vol<br>Contains approx 8.0 std drinks<br>Preservative (220) added<br>750ml</p>
  </section>
</main>
</body>
</html>
```